Kelverin Roofing & Restoration Business Card Design

Lookiing for a double sided business card design that will have rounded corners, will look good with Spot UV, Soft Laminate, or Gloss
Front of card should have Logo, Name and Contact Info, License numbers
Back of card should have Logo, maybe other small details

```html
<!DOCTYPE html>
<html lang="en">
<head>
<meta charset="utf-8">
<title>Kelverin Roofing &amp; Restoration – Business Card</title>
<link href="https://fonts.googleapis.com/css2?family=Montserrat:wght@400;500;600;700&display=swap" rel="stylesheet">
<style>
  :root{
    --stage:#2a2a2a;
    --stage-dark:#141414;
    --card:#1d1d1e;
    --card-edge:#252527;
    --spot-uv:#0e0e0f;
    --ink-white:#f4f5f6;
    --ink-soft:#d8dadc;
    --ink-grey:#8a8b8d;
    --accent:#1ea0e0;
  }
  *{box-sizing:border-box;margin:0;padding:0}
  html,body{width:1200px;height:875px;overflow:hidden}
  body{
    background:radial-gradient(ellipse at 60% 40%,var(--stage) 0%,var(--stage-dark) 100%);
    font-family:"Montserrat",sans-serif;
    position:relative;
  }
  .card{
    position:absolute;top:283px;width:540px;height:309px;
    background:linear-gradient(160deg,var(--card-edge),var(--card));
    border-radius:22px;overflow:hidden;
    box-shadow:0 24px 50px rgba(0,0,0,.55);
  }
  .card--back{left:40px}
  .card--front{left:620px}
  .texture-band{
    position:absolute;left:0;top:0;bottom:0;width:70px;
    background:linear-gradient(90deg,#2b2b2d 0%,#242426 55%,rgba(29,29,30,0) 100%);
  }
  .brand{position:absolute;display:flex;align-items:center}
  .brand-name{font-weight:700;letter-spacing:.5px}
  .brand-dot{width:10px;height:10px;background:var(--accent);margin-left:7px}
  .brand-divider{width:1px;align-self:stretch;margin:0 14px}
  .brand-tagline{font-weight:600;text-transform:uppercase;line-height:1.08;letter-spacing:1px}

  /* back */
  .card--back .brand{left:100px;top:120px;height:70px}
  .card--back .brand-name{font-size:34px;color:var(--ink-grey)}
  .card--back .brand-divider{background:#111}
  .card--back .brand-tagline{font-size:24px;color:var(--spot-uv)}

  /* front */
  .card--front .brand{left:60px;top:54px;height:48px}
  .card--front .brand-name{font-size:26px;color:var(--ink-white)}
  .card--front .brand-divider{background:var(--accent)}
  .card--front .brand-tagline{font-size:15px;color:var(--ink-white)}
  .uv-mark{
    position:absolute;right:22px;top:26px;
    font-size:62px;font-weight:700;color:var(--spot-uv);letter-spacing:1px;
  }
  .address{
    position:absolute;right:34px;top:150px;text-align:right;
    font-size:11px;line-height:1.35;color:var(--ink-soft);
  }
  .rule{position:absolute;left:60px;right:34px;top:190px;height:1px;background:var(--accent)}
  .person{position:absolute;left:60px;top:198px}
  .person-name{font-size:20px;font-weight:700;color:var(--ink-white)}
  .person-name .first{color:var(--accent)}
  .person-role{font-size:11px;color:var(--ink-soft);margin-top:1px}
  .contacts{list-style:none;margin-top:8px}
  .contacts li{display:flex;align-items:center;gap:7px;font-size:11px;color:var(--ink-soft);line-height:1.55}
  .contacts svg{width:10px;height:10px;fill:var(--accent)}
</style>
</head>
<body>

<section class="card card--back" aria-label="Card back">
  <div class="texture-band" role="img" aria-label="Raised spot UV speckle texture"></div>
  <div class="brand">
    <span class="brand-name">Kelverin</span><span class="brand-dot"></span>
    <span class="brand-divider"></span>
    <span class="brand-tagline">Roofing &amp;<br>Restoration</span>
  </div>
</section>

<section class="card card--front" aria-label="Card front">
  <div class="texture-band" role="img" aria-label="Raised spot UV speckle texture"></div>
  <div class="uv-mark">Kelverin</div>
  <div class="brand">
    <span class="brand-name">Kelverin</span><span class="brand-dot"></span>
    <span class="brand-divider"></span>
    <span class="brand-tagline">Roofing &amp;<br>Restoration</span>
  </div>
  <p class="address">12 Marlow Street, # 3 - 5<br>Brenfield, WA 6990</p>
  <div class="rule"></div>
  <div class="person">
    <p class="person-name"><span class="first">Darren</span> Hollis</p>
    <p class="person-role">Managing Director</p>
    <ul class="contacts">
      <li><svg viewBox="0 0 10 10"><path d="M1 2c0-1 1-1.5 2-1.5L4 3 3 4c.6 1.3 1.7 2.4 3 3l1-1 2.5 1c0 1-.5 2-1.5 2C4 9 1 6 1 2z"/></svg>(08) 5550 1427</li>
      <li><svg viewBox="0 0 10 10"><path d="M0 2h10v6H0zM0 2l5 3.5L10 2" stroke="#1d1d1e" stroke-width=".8"/></svg>info@kelverinroofing.com</li>
      <li><svg viewBox="0 0 10 10"><circle cx="5" cy="5" r="4.5"/></svg>www.kelverinroofing.com</li>
    </ul>
  </div>
</section>

</body>
</html>
```